Card for modern wood artisan that builds log homes and timber frames.

Design a card with catchy imagery. With a quick list of things I build and services I offer.

I'd like an English side and a french side. I can provide the text.

I am basically a guy that builds log homes and timber frames , but I am very eco friendly oriented.

I use only eco friendly products to limit my carbon footprint.
I want the client to feel as if they are hiring a good smart builder.

I have been building for a while but just starting out to market myself out there , not just work for other companies. Starting
My own thing legitimately.

I am very conscientious, and I take care of the work I do. I am trying to bring a new age, modern feel to an old profession.

Reason: I am not completely satisfied with A model yet, looking for that masculin rustic artistic design that I havent completely found yet. Thank you for your sumbissions.

Target Market(s)

People looking to hire a builder to design and build their projects.
And contractors that want to hire a quality subcontractor for their jobs.

Industry/Entity Type

Construction

Contact Information for Business Card

I want my logo on it, that I had designed here.
And a list of services I provide.

With my phone number, website adress and Email.

Requirements
Must have
• Artful presentation,
• Eco friendly feel
• I love trees.

```html
<!DOCTYPE html>
<html lang="en">
<head>
<meta charset="UTF-8">
<title>Boisvert Wood Artisan – Business Card</title>
<link rel="stylesheet" href="https://fonts.googleapis.com/css2?family=Mulish:wght@400;600;700&display=swap">
<style>
  :root {
    --backdrop: #2b2b2b;
    --wood-dark: #1e1e1e;
    --wood-mid: #3a3a3a;
    --wood-light: #4d4d4d;
    --paper: #ffffff;
    --ring: rgba(255,255,255,0.18);
    --ink: #222222;
    --ink-soft: #3d3d3d;
    --accent: #f09a1e;
  }
  * { box-sizing: border-box; margin: 0; padding: 0; }
  html, body {
    width: 1200px; height: 791px; overflow: hidden;
    background: var(--backdrop);
    font-family: "Mulish", Arial, sans-serif;
  }
  .canvas {
    position: relative; width: 1200px; height: 791px;
    display: flex; align-items: center; justify-content: center; gap: 40px;
  }
  .card {
    position: relative; width: 540px; height: 309px; overflow: hidden;
    box-shadow: 0 14px 30px rgba(0,0,0,0.5);
  }
  .wood-surface {
    position: absolute; inset: 0;
    background:
      repeating-linear-gradient(160deg, transparent 0 70px, rgba(0,0,0,0.55) 70px 74px, transparent 74px 140px),
      linear-gradient(135deg, var(--wood-light), var(--wood-mid) 45%, var(--wood-dark));
  }

  /* Front */
  .logo-disc {
    position: absolute; left: 50%; top: 50%;
    width: 190px; height: 190px; margin: -95px 0 0 -95px;
    border-radius: 50%; background: var(--paper);
    box-shadow: 0 0 0 14px var(--ring);
    display: flex; flex-direction: column; align-items: center; justify-content: center;
  }
  .brand-name {
    font-weight: 700; font-size: 26px; letter-spacing: 2px; color: var(--ink);
  }
  .brand-tagline {
    margin-top: 6px; font-weight: 600; font-size: 10px; letter-spacing: 2px; color: var(--ink);
  }

  /* Back */
  .info-panel {
    position: absolute; left: 0; right: 0; top: 46px; height: 210px;
    background: var(--paper);
    padding: 34px 40px 0;
  }
  .person-name {
    text-align: center; font-weight: 400; font-size: 40px; letter-spacing: 1px; color: var(--ink);
    line-height: 1;
  }
  .person-name .initial { color: var(--accent); }
  .person-role {
    margin-top: 8px; text-align: center; font-size: 17px; letter-spacing: 1px; color: var(--ink-soft);
  }
  .contact-list {
    list-style: none; display: flex; justify-content: space-between;
    margin-top: 46px;
  }
  .contact-item {
    display: flex; align-items: center; gap: 8px;
    font-size: 13px; color: var(--ink-soft);
  }
  .contact-item svg { width: 20px; height: 20px; fill: var(--accent); flex: none; }
</style>
</head>
<body>
<main class="canvas">

  <section class="card card-front">
    <div class="wood-surface" role="img" aria-label="Dark weathered wood plank texture"></div>
    <div class="logo-disc">
      <span class="brand-name">BOISVERT</span>
      <span class="brand-tagline">WOOD ARTISAN</span>
    </div>
  </section>

  <section class="card card-back">
    <div class="wood-surface" role="img" aria-label="Dark weathered wood plank texture"></div>
    <div class="info-panel">
      <h1 class="person-name"><span class="initial">Y</span>OUR <span class="initial">N</span>AME</h1>
      <p class="person-role">BUSINESS MANAGER</p>
      <ul class="contact-list">
        <li class="contact-item">
          <svg viewBox="0 0 20 20" aria-hidden="true"><path d="M3 7c0-2 3-3 7-3s7 1 7 3v2h-4V7.5c-1-.4-5-.4-6 0V9H3z"/><path d="M5 10h10l1 6H4z"/><circle cx="10" cy="13" r="1.8" fill="#fff"/></svg>
          +00 012 345 678
        </li>
        <li class="contact-item">
          <svg viewBox="0 0 20 20" aria-hidden="true"><rect x="2" y="4" width="16" height="12" rx="1"/><path d="M2.5 5l7.5 6 7.5-6" fill="none" stroke="#fff" stroke-width="1.4"/></svg>
          yourmail@mail.com
        </li>
        <li class="contact-item">
          <svg viewBox="0 0 20 20" aria-hidden="true"><circle cx="10" cy="10" r="8"/><g fill="none" stroke="#fff" stroke-width="1"><ellipse cx="10" cy="10" rx="3.5" ry="8"/><path d="M2 10h16M3.5 6h13M3.5 14h13"/></g></svg>
          www.youwebsite.com
        </li>
      </ul>
    </div>
  </section>

</main>
</body>
</html>
```